A Dedicated Thank You to my Dad

Proposed Dimensions: Approx. 20" x 30"

For Father's Day, I wrote a dedication to my Dad that encapsulates my gratitude for everything he does, and everything he is. His birthday is on August 3, but it is more important for me to transform this dedication into a meaningful and memorable gift than to meet any deadline. I would love an image that captures the relationship between a father and his son, accompanied by my words of thanks in some sort of font that is appropriate for the message (calligprahy? not sure about that).

I had actually posted the Thank You on Pixelmarrow as a public post, so anyone with an account can read it: https://www.pixelmarrow.example/photo.php?fbid=40872219360548813&set=a.318760942157.6650129.3908471&type=1&theater

Only the words starting with "Thank you ..." should be on the poster.

Target Market(s)

This is a personal gift for my Dad. He doesn't have the best of eyesight, so having the words in a really small font would not be particularly helpful. :-)

Requirements
Must have
• * Personable
* Warm
* Inviting
* Memorable
* Understated more favored over Loud
Should not have
• * An entire palette of colors
* Wacky colors or fonts

```html
<!DOCTYPE html>
<html lang="en">
<head>
<meta charset="utf-8">
<title>Thank You — Father's Day Dedication</title>
<link rel="stylesheet" href="https://fonts.googleapis.com/css2?family=Great+Vibes&family=Raleway:wght@400&family=Alegreya+Sans+SC:wght@400&display=swap">
<style>
  :root {
    --bg-deep: #3a1a1c;
    --bg-warm: #c2542f;
    --bg-gold: #d9b24a;
    --bg-rose: #c98a9a;
    --panel: #0f7387;
    --panel-shade: #0c6577;
    --ink: #ffffff;
    --accent: #4fc3e8;
    --frame: #ffffff;
    --pin: #d0121b;
  }
  * { margin: 0; padding: 0; box-sizing: border-box; }
  html, body { width: 800px; height: 1200px; overflow: hidden; }
  body { background: var(--bg-deep); font-family: "Alegreya Sans SC", sans-serif; }

  .poster { position: relative; width: 800px; height: 1200px; overflow: hidden; }

  .backdrop {
    position: absolute; inset: 0;
    background:
      radial-gradient(circle at 12% 28%, var(--bg-gold) 0, transparent 22%),
      radial-gradient(circle at 20% 8%, var(--bg-rose) 0, transparent 25%),
      radial-gradient(circle at 85% 5%, var(--bg-warm) 0, transparent 25%),
      radial-gradient(circle at 30% 95%, var(--bg-warm) 0, transparent 30%),
      radial-gradient(circle at 90% 96%, var(--bg-rose) 0, transparent 25%),
      radial-gradient(circle at 8% 70%, #8e2d2a 0, transparent 30%),
      linear-gradient(160deg, #6b2a24, var(--bg-deep) 55%, #7a3526);
  }

  .message-panel {
    position: absolute; left: 224px; top: 117px; width: 550px; height: 934px;
    background: var(--panel);
    box-shadow: 0 2px 6px rgba(0,0,0,.35);
    color: var(--ink); text-align: center;
  }
  .title {
    position: absolute; left: 0; right: 0; top: 120px;
    font-family: "Great Vibes", cursive; font-weight: 400;
    font-size: 104px; line-height: 0; letter-spacing: 1px;
  }
  .title-rule { position: absolute; left: 149px; top: 131px; }
  .dedicatee {
    position: absolute; left: 0; right: 0; top: 144px;
    font-family: "Raleway", sans-serif; font-size: 17px; letter-spacing: .5px;
    color: var(--accent);
  }
  .verses {
    position: absolute; left: 0; right: 0; top: 187px;
    font-size: 16.5px; line-height: 20.5px; letter-spacing: .3px;
  }
  .verses p { margin-bottom: 20.5px; }
  .closing-flourish {
    position: absolute; left: 245px; top: 917px; width: 70px; height: 30px;
    border-radius: 50%;
    background: radial-gradient(ellipse, #f3e6c8 0, #c9b98a 45%, transparent 72%);
  }

  .snapshot {
    position: absolute; background: var(--frame); padding: 12px;
    box-shadow: 3px 4px 8px rgba(0,0,0,.45);
  }
  .snapshot .photo { width: 100%; height: 100%; }
  .snapshot-father-son { left: 68px; top: 301px; width: 184px; height: 222px; }
  .snapshot-father-son .photo { background: linear-gradient(160deg, #b8a488, #6f6256 50%, #3e4a63); }
  .snapshot-parents { left: 44px; top: 560px; width: 200px; height: 222px; transform: rotate(8deg); }
  .snapshot-parents .photo { background: linear-gradient(170deg, #a9896c, #6e4f3d 45%, #c8bba6); }
  .pin {
    position: absolute; width: 18px; height: 18px; border-radius: 50%;
    background: radial-gradient(circle at 35% 35%, #ff6b6b, var(--pin) 60%, #7d0a0f);
  }
  .pin-one { left: 165px; top: 286px; }
  .pin-two { left: 160px; top: 552px; }
</style>
</head>
<body>
<main class="poster">
  <div class="backdrop" role="img" aria-label="Soft-focus burst of warm red, gold and pink fireworks"></div>

  <figure class="snapshot snapshot-father-son">
    <div class="photo" role="img" aria-label="Photo of a son and his father standing side by side, arm in arm"></div>
  </figure>
  <span class="pin pin-one"></span>

  <figure class="snapshot snapshot-parents">
    <div class="photo" role="img" aria-label="Photo of mother hugging father from behind at home"></div>
  </figure>
  <span class="pin pin-two"></span>

  <section class="message-panel">
    <h1 class="title">Thank You</h1>
    <svg class="title-rule" width="264" height="12" viewBox="0 0 264 12" aria-hidden="true">
      <line x1="14" y1="6" x2="250" y2="6" stroke="var(--accent)" stroke-width="1.5"/>
      <circle cx="8" cy="6" r="3.5" fill="none" stroke="var(--accent)" stroke-width="1.5"/>
      <circle cx="256" cy="6" r="3.5" fill="none" stroke="var(--accent)" stroke-width="1.5"/>
    </svg>
    <p class="dedicatee">DAN WHITLOCK</p>

    <div class="verses">
      <p>Thank you for welcoming<br>more people to stay with us than I can count.</p>
      <p>Thank you for my dry sense of humor.<br>I cherish it.</p>
      <p>Thank you for never giving up<br>on trying to convince me<br>that imperfection is not a failure.</p>
      <p>Thank you for teaching me<br>to try to find the good in everyone.</p>
      <p>Thank you for showing me<br>that there is peace to be found in stillness and quiet.</p>
      <p>Thank you for demonstrating the fun<br>that can be had and the truths<br>that can be gleaned from debate.</p>
      <p>Thank you for accepting me for who I am,<br>no matter who I love, and for helping me to accept myself.</p>
      <p>Thank you for doing whatever you can to help<br>whoever you can, whether friend, family or stranger.</p>
      <p>Thank you for trusting me enough<br>to let your guard down to let me know<br>how you are truly doing.</p>
      <p>Thank you for insisting, year after year,<br>that time with you means more than any gift<br>I could ever purchase. That is one lesson, amongst so many,<br>that I will pass down to our next generation.</p>
    </div>

    <div class="closing-flourish" role="img" aria-label="Small cream floral spray ornament"></div>
  </section>
</main>
</body>
</html>
```